VantoMedix website

I have a plumfield hosting website already & have been using wordpress.
See www.vantomedix-sample.com
I have a logo's already.
I need a front page "VantoMedix". I have 3 products: (need separate pages)
1) the "GlideTray" (can't supply images ATM)
2) the "TubeKeeper" (several stills below & animation: http://www.clipvault-example.com/watch?v=Z7HqR20mW3x&list=QPtr8B_kzoepWnXcM4Lq5B_T&feature=share)
3) the "FastPart" animation here: http://clipv.example/pwrtk-Mmo_E & logo as below

It needs to be corporate & professional looking. VantoMedix is an innovative design house for medical devices.

Reason: Hi Designers, thanks for all your work to date - there have been some great designs. We'll be providing feedback to some of you in the near future. The reason we have extended the deadline is simply that we are too busy with other aspects of the business to focus on this at the moment. Kind regards, the VantoMedix team.

Dear Designers,

VantoMedix apologies for the delay due to our busyness. 
Please help us to understand the process here:
are we getting fully working websites? With multiple pages? Will we be able to modify them?
If not, what is the output?

Kind regards,
the Vanto team.

```html
<!DOCTYPE html>
<html lang="en">
<head>
<meta charset="utf-8">
<title>VantoMedix</title>
<link rel="stylesheet" href="https://fonts.googleapis.com/css2?family=Figtree:wght@400;500;600;700&display=swap">
<style>
:root{
  --blue:#2fa3dc;
  --blue-dark:#1f8fcb;
  --blue-soft:#e3f3fc;
  --orange:#f26a1b;
  --orange-dark:#e45a0d;
  --ink:#3a4450;
  --muted:#9aa3ab;
  --text:#555f68;
  --line:#d7e3ea;
  --green:#5aa72b;
  --white:#ffffff;
}
*{box-sizing:border-box;margin:0;padding:0}
html,body{width:1024px;height:1200px;overflow:hidden}
body{position:relative;font-family:"Figtree",Arial,sans-serif;background:var(--blue-soft);color:var(--text)}
.abs{position:absolute}
a{text-decoration:none;color:inherit}

/* header */
.site-header{left:0;top:0;width:1024px;height:92px;background:linear-gradient(#ffffff,#eef4f8)}
.brand{left:135px;top:22px;display:flex;align-items:center;gap:10px}
.brand-dot{width:30px;height:30px;border-radius:50%;background:var(--orange)}
.brand-name{font-size:38px;font-weight:700;color:var(--blue);letter-spacing:-0.5px}
.call{left:645px;top:40px;display:flex;align-items:center;gap:8px;color:var(--orange);font-size:19px}

/* nav */
.main-nav{left:0;top:92px;width:1024px;height:61px;background:var(--white)}
.nav-item{top:24px;font-size:10.5px;font-weight:600;color:#7b8590;letter-spacing:.2px}
.nav-sep{top:10px;width:1px;height:40px;background:#eceff2}
.nav-active{left:212px;top:13px;width:90px;height:48px;background:var(--blue);color:var(--white);font-size:10.5px;font-weight:600;text-align:center;padding-top:11px}
.social{top:16px;width:26px;height:26px;border-radius:3px}

.dropdown{left:212px;top:135px;width:122px;height:106px;background:var(--blue);z-index:5}
.drop-item{left:18px;font-size:9.5px;font-weight:500;color:var(--white)}
.drop-active{left:0;top:42px;width:122px;height:32px;background:var(--orange)}

/* hero */
.hero{left:0;top:153px;width:1024px;height:428px}
.hero-photo{left:0;top:0;width:1024px;height:428px;background:linear-gradient(100deg,#d9e4ec 0%,#c9d5dd 40%,#e9d6c8 68%,#d6c3b3 85%,#eaf2f7 100%);clip-path:path('M0 0 H1024 V343 Q512 511 0 343 Z')}
.hero-panel{left:0;top:109px;width:534px;height:199px;background:rgba(47,160,219,.95);color:var(--white)}
.hero-title{left:148px;top:34px;font-size:35px;font-weight:600}
.hero-text{left:148px;top:88px;width:360px;font-size:14px;line-height:20px;font-weight:500}

/* cards */
.card{top:619px;width:174px;height:279px;background:var(--white);box-shadow:0 1px 3px rgba(0,0,0,.12)}
.card-head{left:0;top:0;width:174px;height:55px;background:linear-gradient(#5cbfe9,#2fa0db);color:var(--white);font-size:13px;font-weight:600;padding:22px 0 0 16px}
.card-media{left:11px;top:72px;width:151px;height:102px;border-radius:2px}
.card-text{left:13px;top:189px;width:150px;font-size:10px;line-height:14.5px;color:var(--muted)}
.read-more{left:13px;top:252px;font-size:9px;font-weight:700;color:var(--blue)}
.contact-line{left:15px;font-size:10px;color:var(--muted);white-space:nowrap}
.contact-line.mail{font-size:8.6px}
.contact-line a{color:var(--blue)}
.btn-contact{left:26px;top:218px;width:112px;height:36px;border-radius:3px;background:linear-gradient(#fb8a3a,var(--orange-dark));color:var(--white);font-size:12px;font-weight:600;text-align:center;line-height:36px}

/* footer */
.footer{left:0;top:918px;width:1024px;height:234px;background:var(--white);border-top:1px solid var(--line)}
.f-col{top:28px;width:180px}
.f-head{font-size:11.5px;font-weight:700;color:var(--ink);margin-bottom:12px}
.f-text{font-size:10px;line-height:16.8px;color:var(--text)}
.tag{color:#e5452e}
.time{font-size:10px;font-style:italic;color:var(--muted);margin:2px 0 10px}
.email-field{width:177px;height:29px;border:1px solid #d7dde2;font-size:10px;color:var(--muted);padding:8px 7px;margin-top:12px}
.btn-signup{width:73px;height:29px;border-radius:2px;background:linear-gradient(#6cbb38,var(--green));color:var(--white);font-size:10px;font-weight:700;text-align:center;line-height:29px;margin-top:14px}
.nav-list{font-size:10px;line-height:20.8px;color:var(--text)}
.bottom-bar{left:0;top:1152px;width:1024px;height:48px;background:var(--blue-soft);border-top:1px solid var(--line)}
.copyright{left:135px;top:19px;font-size:10px;color:var(--muted)}
.legal{right:135px;top:19px;font-size:10px;font-weight:600;color:var(--ink)}
.legal .hl{color:#e5452e}
.legal .sep{color:#b4bcc3;font-weight:400;margin:0 4px}
</style>
</head>
<body>

<header class="site-header abs">
  <div class="brand abs"><span class="brand-dot"></span><span class="brand-name">VantoMedix</span></div>
  <div class="call abs">
    <svg width="18" height="18" viewBox="0 0 24 24" fill="none" stroke="#5aa9d6" stroke-width="2"><path d="M6 3l3 4-2 2c1 3 4 6 7 7l2-2 4 3-2 4C10 21 3 14 3 5z"/><path d="M15 3a6 6 0 0 1 6 6M15 7a2 2 0 0 1 2 2"/></svg>
    <span>CALL US +1800.555.0199</span>
  </div>
</header>

<nav class="main-nav abs">
  <a class="nav-item abs" style="left:164px">HOME</a>
  <a class="nav-active abs">PRODUCTS</a>
  <a class="nav-item abs" style="left:322px">ABOUT US</a>
  <span class="nav-sep abs" style="left:392px"></span>
  <a class="nav-item abs" style="left:411px">ASK QUESTION</a>
  <span class="nav-sep abs" style="left:507px"></span>
  <a class="nav-item abs" style="left:529px">CONTACT US</a>
  <span class="social abs" style="left:769px;background:#3b5a9a"></span>
  <span class="social abs" style="left:807px;background:#2aa3e0"></span>
  <span class="social abs" style="left:845px;background:#1a6fa8"></span>
</nav>

<div class="dropdown abs">
  <span class="drop-item abs" style="top:26px">GlideTray</span>
  <div class="drop-active abs">
    <span class="drop-item abs" style="top:10px">TubeKeeper IV</span>
    <svg class="abs" style="left:106px;top:10px" width="8" height="12" viewBox="0 0 8 12"><path d="M1 1l5 5-5 5" stroke="#fff" stroke-width="2" fill="none"/></svg>
  </div>
  <span class="drop-item abs" style="top:86px">FastPart</span>
</div>

<section class="hero abs">
  <div class="hero-photo abs" role="img" aria-label="Photo of a smiling medical professional with a stethoscope in front of a blurred team of clinicians"></div>
  <div class="hero-panel abs">
    <h1 class="hero-title abs">VantoMedix</h1>
    <p class="hero-text abs">VantoMedix has created a fully integrated system to help paramedics remove patients from everyday awkward situations:&nbsp; down stairs, around tight corners &amp; out of small rooms.</p>
  </div>
</section>

<article class="card abs" style="left:138px">
  <div class="card-head abs">GlideTray</div>
  <div class="card-media abs" style="background:linear-gradient(#9a9fd6,#b6b9e4)" role="img" aria-label="Rendering of the GlideTray device"></div>
  <p class="card-text abs">Lorem ipsum dolor sit amet, consectetur adipisicing elit, sed do eiusmod tempor incididunt</p>
  <a class="read-more abs">READ MORE</a>
</article>

<article class="card abs" style="left:330px">
  <div class="card-head abs">TubeKeeper IV</div>
  <div class="card-media abs" style="background:linear-gradient(#f4f4f4,#dcdcdc 85%,#222 86%)" role="img" aria-label="Video still of the TubeKeeper IV animation"></div>
  <p class="card-text abs">Lorem ipsum dolor sit amet, consectetur adipisicing elit, sed do eiusmod tempor incididunt</p>
  <a class="read-more abs">READ MORE</a>
</article>

<article class="card abs" style="left:520px">
  <div class="card-head abs">FastPart</div>
  <div class="card-media abs" style="background:linear-gradient(90deg,#5a1414,#3a3a3a 50%,#5a1414);" role="img" aria-label="Video still of the FastPart animation"></div>
  <p class="card-text abs">Lorem ipsum dolor sit amet, consectetur adipisicing elit, sed do eiusmod tempor incididunt</p>
  <a class="read-more abs">READ MORE</a>
</article>

<article class="card abs" style="left:712px">
  <div class="card-head abs">Questions? Contact us!</div>
  <p class="contact-line abs" style="top:70px">Phone: (+39) 2400001111</p>
  <p class="contact-line mail abs" style="top:94px">E-mail: <a>info@vantomedix-sample.com</a></p>
  <p class="contact-line abs" style="top:128px">Brightline, Company Inc.</p>
  <p class="contact-line abs" style="top:151px">4470 Harbor Street</p>
  <p class="contact-line abs" style="top:174px">Oakridge, USA</p>
  <a class="btn-contact abs">Contact Us</a>
</article>

<footer class="footer abs">
  <div class="f-col abs" style="left:135px">
    <h3 class="f-head">ABOUT</h3>
    <p class="f-text">Donec rutrum elit ac arcu bibendum rhoncus in vitae turpis. Quisque fermentum gravida eros non faucibus. Curabitur fermentum, arcu sed cursus commodo.</p>
    <p class="f-text" style="margin-top:11px;line-height:19px">sales@northpixel-sample.com<br>+1 (555) 010 - 20 - 30</p>
  </div>
  <div class="f-col abs" style="left:327px">
    <h3 class="f-head">RECENT TWEETS</h3>
    <p class="f-text"><span class="tag">@vantomedix</span> Vivamus porta dui dapibus erat egestas semper. In quis sem neque <span class="tag">#paramedic #vanto</span></p>
    <p class="time">5 minutes ago</p>
    <p class="f-text"><span class="tag">@vantomedix</span> Vivamus porta dui dapibus erat egestas semper. In quis sem neque <span class="tag">#paramedic #vanto</span></p>
    <p class="time">1 day ago</p>
  </div>
  <div class="f-col abs" style="left:519px">
    <h3 class="f-head">NEWSLETTER SIGNUP</h3>
    <p class="f-text">Donec rutrum elit ac arcu bibendum rhoncus in vitae turpis.</p>
    <div class="email-field">Enter your e-mail address</div>
    <div class="btn-signup">SIGNUP</div>
  </div>
  <div class="f-col abs" style="left:711px">
    <h3 class="f-head">NAVIGATION</h3>
    <p class="nav-list abs" style="top:25px;left:0">Home<br>Products<br>About Us<br>Ask Question<br>Contact Us</p>
    <p class="nav-list abs" style="top:25px;left:97px">GlideTray<br>TubeKeeper IV<br>FastPart</p>
  </div>
</footer>

<div class="bottom-bar abs">
  <p class="copyright abs">Copyright © 2014 VantoMedix. All rights reserved.</p>
  <p class="legal abs">Terms &amp; Conditions<span class="sep">/</span><span class="hl">Privacy Policy</span><span class="sep">/</span>FAQ</p>
</div>

</body>
</html>
```